i need a business card design for my family investment company "qarvenna investments" based in dubai. its a diverse investment firm focusing on education, hospitality and automotive. the design has to be modern and try to incorporate the logo "E" in the design. details on card as follow

Yousef R Bin Hadrami
Managing Director
yousef@qarvenna.ae
www.qarvenna.ae

Harbor zone,falcon tower, office 3817, dubai
tel. 04 7391852
mobile.050 8142903

Target Market(s)

card used for networking events and investor meetings

Industry/Entity Type

Hospitality

```html
<!DOCTYPE html>
<html lang="en">
<head>
<meta charset="utf-8">
<title>Qarvenna Investments – Business Card</title>
<link rel="stylesheet" href="https://fonts.googleapis.com/css2?family=Mulish:wght@300;400;700&display=swap">
<style>
  :root {
    --backdrop: #2b2d31;
    --paper: #f4f4f2;
    --ink-blue: #6c7f9d;
    --ink-grey: #7d8594;
    --bar-tint: #b9c0cc;
    --navy-top: #3b4759;
    --navy-bottom: #27313f;
    --logo-white: #f2f4f7;
  }
  * { box-sizing: border-box; margin: 0; padding: 0; }
  html, body {
    width: 1200px;
    height: 800px;
    overflow: hidden;
    background: var(--backdrop);
    font-family: "Mulish", "Century Gothic", sans-serif;
  }
  .stage {
    width: 1200px;
    height: 800px;
    display: flex;
    align-items: center;
    justify-content: center;
    gap: 40px;
  }
  .card {
    width: 540px;
    height: 309px;
    border-radius: 3px;
    box-shadow: 0 10px 30px rgba(0,0,0,0.35);
    position: relative;
    overflow: hidden;
  }
  /* Contact side */
  .card--contact {
    background: var(--paper);
    padding: 30px 34px;
    color: var(--ink-blue);
  }
  .holder-name {
    font-size: 21px;
    font-weight: 700;
    color: var(--ink-blue);
    letter-spacing: 0.2px;
  }
  .holder-title {
    font-size: 12px;
    font-weight: 400;
    color: var(--ink-grey);
    margin-top: 2px;
  }
  .contact-list {
    list-style: none;
    margin-top: 14px;
  }
  .contact-item {
    display: flex;
    align-items: center;
    gap: 10px;
    font-size: 15px;
    font-weight: 400;
    line-height: 25px;
    color: var(--ink-blue);
    white-space: nowrap;
  }
  .contact-icon {
    width: 15px;
    height: 15px;
    flex: none;
    fill: var(--ink-blue);
  }
  .accent-bar {
    position: absolute;
    right: 0;
    height: 14px;
    width: 100px;
    background: var(--bar-tint);
  }
  .accent-bar--upper { top: 150px; right: 12px; }
  .accent-bar--middle { top: 205px; right: 6px; }
  .accent-bar--lower { top: 262px; right: 0; }
  /* Brand side */
  .card--brand {
    background: linear-gradient(160deg, var(--navy-top) 0%, var(--navy-bottom) 100%);
    display: flex;
    align-items: center;
    justify-content: center;
  }
  .brand-name {
    font-size: 28px;
    font-weight: 300;
    color: var(--logo-white);
    letter-spacing: 8px;
    text-transform: uppercase;
  }
</style>
</head>
<body>
<main class="stage">
  <section class="card card--contact" aria-label="Contact side">
    <h1 class="holder-name">Yousef R Bin Hadrami</h1>
    <p class="holder-title">Managing Director</p>
    <ul class="contact-list">
      <li class="contact-item">
        <svg class="contact-icon" viewBox="0 0 16 16" aria-hidden="true"><path d="M1 3.5h14v9.5H1zM2 4.5v.3l6 4.4 6-4.4v-.3z"/></svg>
        <span>yousef@qarvenna.ae</span>
      </li>
      <li class="contact-item">
        <svg class="contact-icon" viewBox="0 0 16 16" aria-hidden="true"><path d="M4.5 1h7a1 1 0 0 1 1 1v12a1 1 0 0 1-1 1h-7a1 1 0 0 1-1-1V2a1 1 0 0 1 1-1zm.5 2v8h6V3zm3 9.2a.8.8 0 1 0 0 1.6.8.8 0 0 0 0-1.6z"/></svg>
        <span>050 8142903</span>
      </li>
      <li class="contact-item">
        <svg class="contact-icon" viewBox="0 0 16 16" aria-hidden="true"><path d="M3.6 1.2l2.2 2.6-1.3 1.6c.8 2.2 2.8 4.2 5 5l1.6-1.3 2.6 2.2-1.5 2.5C7 13.5 2.5 9 1.1 2.7z"/></svg>
        <span>04 7391852</span>
      </li>
      <li class="contact-item">
        <svg class="contact-icon" viewBox="0 0 16 16" aria-hidden="true"><circle cx="8" cy="8" r="6.5" fill="none" stroke="#6c7f9d" stroke-width="1.3"/><path d="M1.5 8h13M8 1.5v13" stroke="#6c7f9d" stroke-width="1.1"/><ellipse cx="8" cy="8" rx="3" ry="6.5" fill="none" stroke="#6c7f9d" stroke-width="1.1"/></svg>
        <span>www.qarvenna.ae</span>
      </li>
      <li class="contact-item">
        <svg class="contact-icon" viewBox="0 0 16 16" aria-hidden="true"><path d="M2 15V5h5V1h7v14zM3.5 7v1.5H5V7zm0 3v1.5H5V10zm5-7v1.5H10V3zm2.5 0v1.5h1.5V3zM8.5 6v1.5H10V6zM11 6v1.5h1.5V6zM8.5 9v1.5H10V9zM11 9v1.5h1.5V9z"/></svg>
        <span>Harbor Zone, Falcon Tower, Office 3817, DUBAI</span>
      </li>
    </ul>
    <span class="accent-bar accent-bar--upper" aria-hidden="true"></span>
    <span class="accent-bar accent-bar--middle" aria-hidden="true"></span>
    <span class="accent-bar accent-bar--lower" aria-hidden="true"></span>
  </section>

  <section class="card card--brand" aria-label="Brand side">
    <p class="brand-name">Qarvenna Investments</p>
  </section>
</main>
</body>
</html>
```